Business Card

Please design a business card with our logo on a cream coloured background and include the following information:

Tallowmere Shopping Centre
ph (08) 9341 7086

sales@velvetpetalblooms.com

www.velvetpetalblooms.com

on reverse:

Find us on Facebook
facebook.com/velvetpetalblooms

```html
<!DOCTYPE html>
<html lang="en">
<head>
<meta charset="utf-8">
<title>Velvet Petal Blooms – Business Card</title>
<link rel="stylesheet" href="https://fonts.googleapis.com/css2?family=Signika:wght@400;600&display=swap">
<style>
  :root {
    --page: #ffffff;
    --cream: #f3f0d2;
    --card-edge: #d9d5b4;
    --leaf-green: #5d7d2c;
    --ink: #3a3830;
    --olive: #5e5b34;
  }
  html, body {
    margin: 0;
    padding: 0;
    width: 872px;
    height: 1200px;
    overflow: hidden;
    background: var(--page);
    font-family: "Signika", sans-serif;
  }
  .canvas {
    position: relative;
    width: 872px;
    height: 1200px;
  }
  .card {
    position: absolute;
    left: 4px;
    width: 864px;
    background: var(--cream);
    border: 1px solid var(--card-edge);
    box-sizing: border-box;
  }
  .card--front { top: 8px; height: 554px; }
  .card--back { top: 644px; height: 554px; }

  .brand-name {
    position: absolute;
    margin: 0;
    font-weight: 600;
    white-space: nowrap;
  }
  .card--front .brand-name {
    left: 0;
    right: 0;
    top: 192px;
    text-align: center;
    font-size: 64px;
    color: var(--leaf-green);
  }
  .facebook-link {
    position: absolute;
    left: 0;
    right: 0;
    top: 362px;
    margin: 0;
    text-align: center;
    font-size: 30px;
    font-weight: 600;
    color: var(--ink);
  }

  .brand-dot {
    position: absolute;
    left: 583px;
    top: 76px;
    width: 82px;
    height: 82px;
    border-radius: 50%;
    background: var(--leaf-green);
  }
  .card--back .brand-name {
    left: 466px;
    top: 170px;
    font-size: 42px;
    color: var(--ink);
  }
  .contact {
    position: absolute;
    left: 74px;
    margin: 0;
    color: var(--olive);
  }
  .contact--location { top: 274px; font-size: 27px; font-weight: 600; }
  .contact--phone { top: 310px; font-size: 19px; font-weight: 600; }
  .contact--email { top: 378px; font-size: 19px; }
  .contact--web { top: 464px; font-size: 19px; color: var(--ink); }
</style>
</head>
<body>
<main class="canvas">
  <section class="card card--front" aria-label="Card reverse">
    <p class="brand-name">Velvet Petal Blooms</p>
    <p class="facebook-link">facebook.com/velvetpetalblooms</p>
  </section>

  <section class="card card--back" aria-label="Card face">
    <span class="brand-dot" aria-hidden="true"></span>
    <p class="brand-name">Velvet Petal Blooms</p>
    <p class="contact contact--location">Tallowmere Shopping Centre</p>
    <p class="contact contact--phone">ph (08) 9341 7086</p>
    <p class="contact contact--email">sales@velvetpetalblooms.com</p>
    <p class="contact contact--web">www.velvetpetalblooms.com</p>
  </section>
</main>
</body>
</html>
```